Insurtech company need a banner design in an exhibition

We need a poster design for event exhibition with the size of 2000mm height and 850mm width.

The feeling of the design should be peaceful, smart and secure, also relate it to the insurance industry.

Banner shouldn't be a lot of text, should be simple, clean and easy to read.

For the color theme, please follow our website: http://veltrapine.com

Our company, BrivaForge provides mobile and AI solutions for insurance companies and claims handling companies.

More detail description, you can check out our website as I mentioned above.

Example of size model 850:
http://www.quellmarkstands.com.au/images/html_zero_pix1.gif
Updates

Target Market(s)

Corporate companies, insurance companies, claims handling companies, major retailers

Industry/Entity Type

Insurance

Logo Text

Briva Forge

Font styles to use
Other font styles liked:
• Roboto or suitable font style

Requirements
Must have
• Mobile, Video lives streaming & Artificial intelligent
• Please follow the color theme of our website: http://veltrapine.com
Nice to have
• Professional and techy feeling, try to relate to insurance

```html
<!DOCTYPE html>
<html lang="en">
<head>
<meta charset="utf-8">
<title>Briva Forge – Exhibition Banner</title>
<link href="https://fonts.googleapis.com/css2?family=Roboto+Condensed:wght@300;700&display=swap" rel="stylesheet">
<style>
  :root {
    --page-bg: #ececec;
    --brand-blue: #0a5ad6;
    --band-blue-top: #0b7be8;
    --band-blue-bottom: #0058d0;
    --white: #ffffff;
    --art-light: #e4e4e4;
    --art-mid: #8a8a8a;
    --art-dark: #1c1c1c;
    --art-deep: #2a2a2a;
  }
  * { box-sizing: border-box; margin: 0; padding: 0; }
  html, body {
    width: 1200px;
    height: 848px;
    overflow: hidden;
    background: var(--page-bg);
  }
  .canvas {
    position: relative;
    width: 1200px;
    height: 848px;
  }
  .banner {
    position: absolute;
    left: 430px;
    top: 24px;
    width: 340px;
    height: 800px;
    background: var(--white);
    overflow: hidden;
    font-family: "Roboto Condensed", sans-serif;
  }
  .banner__artwork {
    position: absolute;
    inset: 0;
    background:
      linear-gradient(160deg, var(--art-light) 0%, #bdbdbd 22%, var(--art-mid) 38%, var(--art-dark) 60%, var(--art-deep) 80%, #3a3a3a 100%);
  }
  .banner__top-bar {
    position: absolute;
    left: 0;
    top: 0;
    width: 100%;
    height: 22px;
    background: var(--brand-blue);
  }
  .logo-box {
    position: absolute;
    left: 92px;
    top: 4px;
    width: 152px;
    height: 112px;
    background: var(--white);
    box-shadow: 0 2px 6px rgba(0,0,0,0.25);
    display: flex;
    align-items: center;
    justify-content: center;
    gap: 7px;
  }
  .logo-box__dot {
    width: 14px;
    height: 14px;
    border-radius: 50%;
    background: var(--brand-blue);
    flex: none;
  }
  .logo-box__name {
    font-weight: 700;
    font-size: 22px;
    color: var(--brand-blue);
    white-space: nowrap;
  }
  .headline {
    position: absolute;
    left: 0;
    top: 440px;
    width: 100%;
    color: var(--white);
    text-transform: uppercase;
  }
  .headline__line {
    display: block;
    padding-left: 14px;
    font-size: 56px;
    line-height: 47px;
    letter-spacing: -1.5px;
    white-space: nowrap;
  }
  .headline__line--bold { font-weight: 700; }
  .headline__line--light { font-weight: 300; }
  .headline__band {
    margin-top: 4px;
    padding: 3px 0 4px;
    width: 332px;
    background: linear-gradient(180deg, var(--band-blue-top), var(--band-blue-bottom));
  }
</style>
</head>
<body>
  <main class="canvas">
    <section class="banner" aria-label="Briva Forge exhibition banner">
      <div class="banner__artwork" role="img" aria-label="Abstract layered grey fan shapes fading from light grey at top to charcoal at bottom"></div>
      <div class="banner__top-bar"></div>
      <div class="logo-box">
        <span class="logo-box__dot"></span>
        <span class="logo-box__name">Briva Forge</span>
      </div>
      <h1 class="headline">
        <span class="headline__line headline__line--bold">Mobile</span>
        <span class="headline__line headline__line--light">Video Lives</span>
        <span class="headline__line headline__line--light">Streaming</span>
        <span class="headline__band">
          <span class="headline__line headline__line--bold">&amp; Artificial</span>
          <span class="headline__line headline__line--bold">Intelligent</span>
        </span>
      </h1>
    </section>
  </main>
</body>
</html>
```